Email Notification & Marketing Templates

I want to start with something like a newsletter or informational email, but i need Top Tips to Detect Phishing Scams. Something that i can send to users so they can follow it when receiving or exchanging emails. I will also need promotional items for my company that i can send to customers as well. It can be based on on our website PLVORIX.COM

Will also need:
newsletters
announcements
marketing emails
alerts
security notifications

Examples:Items such as Security Awareness Poster Series
Phishing Awareness
Password Security
Email Attachments
QR Code scams
Public WiFi safety

```html
<!DOCTYPE html>
<html lang="en">
<head>
<meta charset="utf-8">
<title>5 Red Flags to Identify Phishing Scams — Plvorix</title>
<link rel="stylesheet" href="https://fonts.googleapis.com/css2?family=Audiowide&family=Montserrat:wght@400;500;600;700;800&display=swap">
<style>
  :root {
    --black: #000000;
    --ink: #1c1c1c;
    --white: #ffffff;
    --grey: #b9b9b9;
    --green-deep: #0f7a2c;
    --green: #2fae3c;
    --lime: #8fd53a;
    --lime-bright: #9edc3c;
    --red: #e8332a;
    --art-green: #5fbf4a;
    --art-pale: #e6ece6;
  }
  * { box-sizing: border-box; margin: 0; padding: 0; }
  html, body { width: 1200px; height: 3000px; overflow: hidden; background: var(--black); }
  body { position: relative; font-family: "Montserrat", sans-serif; color: var(--ink); }

  .header { position: absolute; left: 0; top: 0; width: 1200px; height: 160px; background: var(--black); }
  .brand { position: absolute; left: 90px; top: 62px; display: flex; align-items: center; gap: 18px; }
  .brand-mark { width: 44px; height: 44px; background: var(--lime); }
  .brand-name { font-family: "Montserrat", sans-serif; font-weight: 800; font-size: 52px; color: var(--lime); letter-spacing: 2px; }
  .service-tag { position: absolute; right: 76px; top: 74px; text-align: right; font-weight: 700; font-size: 30px; line-height: 36px; color: var(--grey); }

  .hero { position: absolute; left: 0; top: 160px; width: 1200px; height: 590px;
    background: linear-gradient(100deg, var(--green-deep) 0%, var(--green) 45%, var(--lime) 100%); }
  .hero-title { position: absolute; left: 66px; top: 170px; color: var(--white); font-family: "Audiowide", sans-serif; text-transform: uppercase; }
  .hero-title .big { display: block; font-size: 128px; line-height: 112px; letter-spacing: 2px; }
  .hero-title .mid { display: block; font-size: 66px; line-height: 68px; margin-top: 10px; }
  .hero-title .small { display: block; font-size: 50px; line-height: 58px; }
  .hero-art { position: absolute; left: 690px; top: 170px; width: 500px; height: 420px; }

  .flags { position: absolute; left: 0; top: 750px; width: 1200px; height: 960px; background: var(--white); }
  .flag { position: absolute; left: 0; width: 1200px; }
  .flag-icon { position: absolute; left: 80px; top: 0; width: 100px; height: 100px; }
  .flag-body { position: absolute; left: 296px; top: 0; width: 840px; }
  .flag-title { font-weight: 700; font-size: 38px; line-height: 46px; color: var(--ink); margin-bottom: 12px; }
  .flag-text { font-weight: 500; font-size: 24px; line-height: 34px; color: var(--ink); }
  .flag-text strong { font-weight: 700; }

  .safety { position: absolute; left: 0; top: 1710px; width: 1200px; height: 1210px; background: var(--black); }
  .safety-title { position: absolute; left: 58px; top: 82px; font-family: "Audiowide", sans-serif; font-size: 104px; line-height: 104px; color: var(--lime-bright); text-transform: uppercase; }
  .safety-art { position: absolute; left: 600px; top: 40px; width: 600px; height: 380px; }
  .tip { position: absolute; width: 470px; }
  .tip-title { font-weight: 800; font-size: 38px; line-height: 44px; color: var(--lime-bright); margin-bottom: 34px; letter-spacing: -0.5px; }
  .tip-text { font-weight: 400; font-size: 22px; line-height: 30px; color: var(--white); letter-spacing: -0.3px; }

  .footer { position: absolute; left: 0; top: 2920px; width: 1200px; height: 80px;
    background: linear-gradient(100deg, var(--green-deep) 0%, var(--green) 40%, var(--lime) 100%);
    display: flex; align-items: center; justify-content: center; }
  .footer-text { font-weight: 700; font-size: 36px; color: var(--white); letter-spacing: 3px; }
</style>
</head>
<body>

<header class="header">
  <div class="brand">
    <span class="brand-mark"></span>
    <span class="brand-name">PLVORIX</span>
  </div>
  <div class="service-tag">Managed<br>IT Services</div>
</header>

<section class="hero">
  <h1 class="hero-title">
    <span class="big">5 Red</span>
    <span class="big">Flags</span>
    <span class="mid">To Identify</span>
    <span class="small">Phishing Scams</span>
  </h1>
  <div class="hero-art" role="img" aria-label="Illustration of a person with a laptop beside a large screen showing an email envelope, login form and chat bubbles"
       style="background: radial-gradient(ellipse at 60% 55%, rgba(230,236,230,0.85) 0%, rgba(95,191,74,0.6) 55%, rgba(95,191,74,0) 75%);"></div>
</section>

<section class="flags">
  <article class="flag" style="top: 96px;">
    <svg class="flag-icon" viewBox="0 0 100 100" aria-hidden="true">
      <g stroke="var(--red)" stroke-width="5" stroke-linecap="round">
        <line x1="50" y1="4" x2="50" y2="16"/><line x1="20" y1="14" x2="27" y2="24"/><line x1="80" y1="14" x2="73" y2="24"/>
        <line x1="6" y1="40" x2="18" y2="42"/><line x1="94" y1="40" x2="82" y2="42"/>
      </g>
      <path d="M26 78 V54 a24 24 0 0 1 48 0 V78 Z" fill="var(--red)"/>
      <rect x="18" y="78" width="64" height="12" rx="3" fill="var(--red)"/>
      <circle cx="50" cy="56" r="7" fill="var(--white)"/>
      <rect x="47" y="60" width="6" height="14" fill="var(--white)"/>
    </svg>
    <div class="flag-body">
      <h2 class="flag-title">Sense of Urgency or Threats</h2>
      <p class="flag-text">Scammers often demand immediate action, such as <strong>"your account will be suspended"</strong> or "<strong>urgent payment required</strong>," to pressure you into skipping safety checks.</p>
    </div>
  </article>

  <article class="flag" style="top: 268px;">
    <svg class="flag-icon" viewBox="0 0 100 100" aria-hidden="true">
      <path d="M6 40 L50 8 L94 40 V92 H6 Z" fill="var(--red)"/>
      <path d="M6 40 L50 70 L94 40" fill="none" stroke="var(--white)" stroke-width="3"/>
      <circle cx="50" cy="40" r="20" fill="var(--white)"/>
      <circle cx="50" cy="40" r="14" fill="none" stroke="var(--red)" stroke-width="5"/>
      <line x1="40" y1="30" x2="60" y2="50" stroke="var(--red)" stroke-width="5"/>
    </svg>
    <div class="flag-body">
      <h2 class="flag-title">Suspicious Sender Address</h2>
      <p class="flag-text"><strong>Check the "from" email address carefully.</strong> It may look official but contain <strong>subtle misspellings, use a different domain</strong> (e.g., using @mailhub.com instead of @bank.com), or not match the organization.</p>
    </div>
  </article>

  <article class="flag" style="top: 472px;">
    <svg class="flag-icon" viewBox="0 0 100 100" aria-hidden="true">
      <g stroke="var(--red)" stroke-width="5" stroke-linecap="round">
        <line x1="30" y1="6" x2="32" y2="18"/><line x1="10" y1="20" x2="20" y2="27"/><line x1="50" y1="14" x2="44" y2="24"/><line x1="6" y1="42" x2="18" y2="42"/>
      </g>
      <path d="M30 30 L30 92 L46 76 L58 98 L70 92 L58 70 L80 70 Z" fill="var(--red)"/>
    </svg>
    <div class="flag-body">
      <h2 class="flag-title">Hover Before You Click</h2>
      <p class="flag-text"><strong>Hover your mouse over any links or buttons to see the actual destination</strong> URL in the bottom corner of your browser. If it doesn't match the expected website, it is likely a scam.</p>
    </div>
  </article>

  <article class="flag" style="top: 672px;">
    <svg class="flag-icon" viewBox="0 0 100 100" aria-hidden="true">
      <path d="M66 30 L30 66 a10 10 0 0 0 14 14 L82 42 a18 18 0 0 0 -26 -26 L16 56 a26 26 0 0 0 36 36 L80 64"
            fill="none" stroke="var(--red)" stroke-width="8" stroke-linecap="round"/>
    </svg>
    <div class="flag-body">
      <h2 class="flag-title">Unusual Attachments or Links</h2>
      <p class="flag-text">Be wary of <strong>unexpected attachments, especially .zip, .exe, or office documents,</strong> which can contain malware.</p>
    </div>
  </article>

  <article class="flag" style="top: 834px;">
    <svg class="flag-icon" viewBox="0 0 100 100" aria-hidden="true">
      <path d="M26 4 H44 L54 36 H40 Z M56 4 H74 L60 36 L50 30 Z" fill="var(--ink)"/>
      <circle cx="50" cy="64" r="32" fill="var(--ink)"/>
      <circle cx="50" cy="64" r="24" fill="var(--white)"/>
      <circle cx="50" cy="64" r="19" fill="var(--ink)"/>
      <path d="M50 52 L54 61 L63 61 L56 67 L58 76 L50 71 L42 76 L44 67 L37 61 L46 61 Z" fill="var(--red)"/>
    </svg>
    <div class="flag-body">
      <h2 class="flag-title">Too-Good-To-Be-True Offers</h2>
      <p class="flag-text">Scams may promise <strong>unrealistic deals, prizes, or unexpected money,</strong> designed to lure you into clicking.</p>
    </div>
  </article>
</section>

<section class="safety">
  <h2 class="safety-title">How to<br>be safe</h2>
  <div class="safety-art" role="img" aria-label="Illustration of a person using a large phone screen with a fingerprint unlock, padlock and shield icons"
       style="background: radial-gradient(ellipse at 55% 50%, var(--art-pale) 0%, #cfd6cf 45%, rgba(0,0,0,0) 72%);"></div>

  <div class="tip" style="left: 60px; top: 410px;">
    <h3 class="tip-title">Verify<br>Independently</h3>
    <p class="tip-text">If you receive an urgent alert from a company, do not use the contact information in the email. Instead, find the company's official phone number or website separately.</p>
  </div>
  <div class="tip" style="left: 670px; top: 410px;">
    <h3 class="tip-title">Enable Multi-Factor Authentication (MFA)</h3>
    <p class="tip-text">Set up MFA on all accounts, which provides a layer of security even if a password is stolen.</p>
  </div>
  <div class="tip" style="left: 60px; top: 936px;">
    <h3 class="tip-title">Check<br>for https://</h3>
    <p class="tip-text">Legitimate websites use secure, encrypted connections, though this alone does not guarantee a site is safe.</p>
  </div>
  <div class="tip" style="left: 670px; top: 936px;">
    <h3 class="tip-title">Use Browser<br>Security</h3>
    <p class="tip-text">Browser password managers will often not auto-fill credentials on a fake phishing site, acting as a red flag.</p>
  </div>
</section>

<footer class="footer">
  <p class="footer-text">www.plvorix.com | (555) 014-2290</p>
</footer>

</body>
</html>
```